Contemporary new French wine brand needs logo and series of label design

to design a new contemporary logo and series of labels for a new French wine brand. We hope to attract not just current French wine drinkers but new ones who may appreciate a less traditional and more modern style.
Updates

Reason: we are wanting to extend the project for a few days more to receive more submissions since we had fewer designs submitted than we were expecting, maybe because of the holidays.

Target Market(s)

people who follow the arts community (eg. music, theatre, visual/video arts, dance) --- all mature ages.

Industry/Entity Type

French Wine

Requirements
Must have
• a clear, memorable treatment for the name CLAVINE with accompanying logo.
Nice to have
• embossing, matte/gloss refinement, tasteful foil stamping, coated stock for the whites to help the integrity of the paper in and out of ice buckets. A combo of say, three types of fonts; a semi custom font for the brand name Clavine and maybe a script and one other.
Should not have
• not traditional French

```html
<!DOCTYPE html>
<html lang="fr">
<head>
<meta charset="utf-8">
<title>Clavine – Sauvignon Blanc label</title>
<link rel="stylesheet" href="https://fonts.googleapis.com/css2?family=Josefin+Sans:wght@300&family=Kaushan+Script&display=swap">
<style>
  :root {
    --backdrop: #c4c4c4;
    --label-white: #ffffff;
    --label-edge: #9a9a9a;
    --ink-black: #0b0b0b;
    --glass-pale: #f4f1e6;
    --wine-straw: #e9e2c4;
    --brand-orange: #ec7a1c;
    --variety-grey: #4a4a4a;
  }
  * { box-sizing: border-box; margin: 0; padding: 0; }
  html, body {
    width: 900px;
    height: 1200px;
    overflow: hidden;
    background: var(--backdrop);
  }
  .canvas {
    position: relative;
    width: 900px;
    height: 1200px;
    background: var(--backdrop);
  }
  .label-shape {
    position: absolute;
    left: 0;
    top: 0;
    width: 900px;
    height: 1200px;
  }
  .label-brand {
    position: absolute;
    left: 230px;
    top: 850px;
    font-family: "Kaushan Script", cursive;
    font-weight: 400;
    font-size: 132px;
    line-height: 1;
    color: var(--brand-orange);
  }
  .label-variety {
    position: absolute;
    left: 300px;
    top: 1010px;
    font-family: "Josefin Sans", sans-serif;
    font-weight: 300;
    font-size: 22px;
    letter-spacing: 0.28em;
    text-transform: uppercase;
    color: var(--variety-grey);
  }
</style>
</head>
<body>
  <main class="canvas">
    <svg class="label-shape" viewBox="0 0 900 1200" width="900" height="1200" aria-hidden="false">
      <defs>
        <linearGradient id="artwork-tone" x1="0" y1="0" x2="0" y2="1">
          <stop offset="0" stop-color="#f4f1e6"/>
          <stop offset="0.28" stop-color="#e9e2c4"/>
          <stop offset="0.45" stop-color="#5a5850"/>
          <stop offset="0.6" stop-color="#0b0b0b"/>
          <stop offset="1" stop-color="#0b0b0b"/>
        </linearGradient>
      </defs>
      <path class="label-body" d="M190 150 L740 118 L740 1080 L110 1080 L110 590 L190 590 Z"
            fill="#ffffff" stroke="#9a9a9a" stroke-width="3"/>
      <path class="label-artwork" role="img"
            aria-label="Black silhouette of a hand holding a wine glass of pale white wine by its stem"
            d="M300 180 L620 170 L660 420 L740 470 L740 720 L640 800 L112 830 L112 610 L300 560 Z"
            fill="url(#artwork-tone)"/>
    </svg>
    <h1 class="label-brand">Clavine</h1>
    <p class="label-variety">Sauvignon Blanc</p>
  </main>
</body>
</html>
```